Valmora Holdings - Tidal Crest Car Wash automatic car wash signage

We are wanting to have a new automatic car wash sign designed. Our current one is dated and there are numerous options that are no longer available. We like the look of a clean sharp design in keeping with the Tidal Crest colours; orange and blues. The sign should have the Ultimate and Premium options, the "Tidal Crest" and Tidal Crest Car Wash designed in a clean, concise and cool manner.

Font styles to use
Sans Serif

Colors
f37122
3276b5
0255a3
34a7d8

Requirements
Must have
• This project must have the Ultimate and Premium options, the "bucket" and the Tidal Crest Car Wash title. The orange is a key colour with blues for water.

```html
<!DOCTYPE html>
<html lang="en">
<head>
<meta charset="utf-8">
<title>Tidal Crest Car Wash – Menu Sign</title>
<link href="https://fonts.googleapis.com/css2?family=Montserrat:wght@500;600;700;800&display=swap" rel="stylesheet">
<style>
  :root {
    --orange: #f37122;
    --orange-row: #e2602f;
    --blue-deep: #0255a3;
    --blue-mid: #3276b5;
    --blue-light: #34a7d8;
    --navy: #24448a;
    --ink: #111111;
    --white: #ffffff;
    --page: #dcdcdc;
  }
  * { box-sizing: border-box; margin: 0; padding: 0; }
  html, body { width: 945px; height: 1200px; overflow: hidden; }
  body {
    background: var(--page);
    font-family: "Montserrat", sans-serif;
    position: relative;
  }
  .sign {
    position: absolute;
    left: 20px; top: 381px;
    width: 905px; height: 438px;
    overflow: hidden;
    background: var(--navy);
  }
  .water-backdrop {
    position: absolute; left: 0; top: 0; width: 905px; height: 383px;
    background:
      radial-gradient(ellipse at 30% 55%, rgba(255,255,255,.85) 0%, rgba(255,255,255,.45) 35%, rgba(255,255,255,0) 70%),
      linear-gradient(180deg, var(--blue-mid) 0%, var(--blue-light) 45%, #7cc7ea 100%);
  }
  .header-band {
    position: absolute; left: 0; top: 0; width: 905px; height: 95px;
    background: linear-gradient(90deg, var(--blue-deep), var(--blue-mid) 50%, var(--blue-light));
  }
  .brand-badge {
    position: absolute; left: 31px; top: 6px;
    width: 86px; height: 86px; border-radius: 50%;
    background: var(--white);
    display: flex; align-items: center; justify-content: center;
    text-align: center;
    font-weight: 800; font-size: 14px; line-height: 1.1;
    color: var(--orange);
  }
  .title {
    position: absolute; left: 136px; top: 2px; width: 750px;
    font-family: "Montserrat", sans-serif;
    font-weight: 800;
    font-size: 54px; line-height: 90px;
    color: var(--orange);
    white-space: nowrap;
    text-align: center;
  }
  .feature-list {
    position: absolute; left: 32px; top: 120px; width: 513px;
    list-style: none;
    border-left: 1px solid rgba(255,255,255,.9);
  }
  .feature-list li {
    height: 24.9px; line-height: 26px;
    padding-left: 14px;
    font-size: 19.5px; font-weight: 600;
    color: var(--ink);
    border-bottom: 1px solid rgba(255,255,255,.9);
    white-space: nowrap;
  }
  .package {
    position: absolute; top: 89px; width: 156px;
  }
  .package.ultimate { left: 545px; }
  .package.premium { left: 717px; }
  .package-label {
    height: 31px; background: var(--ink); color: var(--white);
    display: flex; align-items: center; justify-content: center; gap: 6px;
    font-weight: 800; font-size: 13px;
  }
  .package-label .price { font-size: 18px; }
  .package-label .price span { color: var(--orange); font-size: 21px; }
  .package-rows { list-style: none; }
  .package-rows li {
    height: 24.9px; background: var(--orange-row);
    border-bottom: 1px solid rgba(255,255,255,.55);
    display: flex; align-items: center; justify-content: center;
  }
  .package-rows svg { width: 17px; height: 17px; }
  .car-photo {
    position: absolute; left: 367px; top: 330px; width: 164px; height: 82px;
    border-radius: 40px 50px 14px 14px;
    background: linear-gradient(180deg, #4a6a96, #1e2f4c);
  }
  .call-box {
    position: absolute; left: 32px; top: 392px; width: 328px; height: 38px;
    background: var(--orange); color: var(--white);
    font-size: 27px; font-weight: 600; line-height: 38px; text-align: center;
    white-space: nowrap;
  }
  .website {
    position: absolute; left: 555px; top: 398px;
    color: var(--white); font-size: 18px; font-weight: 600;
    white-space: nowrap;
  }
</style>
</head>
<body>
<svg width="0" height="0" style="position:absolute" aria-hidden="true">
  <symbol id="tick" viewBox="0 0 20 20">
    <circle cx="10" cy="10" r="10" fill="#ffffff"/>
    <path d="M5.5 10.3l3 3 6-6.3" fill="none" stroke="#e2602f" stroke-width="2.6" stroke-linecap="round" stroke-linejoin="round"/>
  </symbol>
</svg>

<section class="sign">
  <div class="water-backdrop" role="img" aria-label="Blue water bubbles and droplets background"></div>
  <div class="header-band"></div>

  <div class="brand-badge">Tidal<br>Crest</div>
  <h1 class="title">Tidal Crest Car Wash</h1>

  <ul class="feature-list">
    <li>WINDSHIELD &amp; FRONT END BUG WASH</li>
    <li>UNDER CARRIAGE &amp; WHEEL BLASTER</li>
    <li>EXTRA PASS OF HIGH PRESSURE WASH</li>
    <li>TRY FOAM CONDITIONER I CLEANER</li>
    <li>SIDE KICK DRYERS</li>
    <li>WAX/SURFACE PROTECTANT</li>
    <li>ON BOARD OVERHEAD DRYER</li>
    <li>TWO PASSES OF PRE-SOAK</li>
    <li>HIGH PRESSURE WASH PASS</li>
    <li>SPOT FREE RIMSE</li>
  </ul>

  <div class="package ultimate">
    <div class="package-label">Ultimate <b class="price"><span>$</span>14.00</b></div>
    <ul class="package-rows">
      <li><svg><use href="#tick"/></svg></li>
      <li><svg><use href="#tick"/></svg></li>
      <li><svg><use href="#tick"/></svg></li>
      <li><svg><use href="#tick"/></svg></li>
      <li><svg><use href="#tick"/></svg></li>
      <li><svg><use href="#tick"/></svg></li>
      <li><svg><use href="#tick"/></svg></li>
      <li><svg><use href="#tick"/></svg></li>
      <li><svg><use href="#tick"/></svg></li>
      <li><svg><use href="#tick"/></svg></li>
    </ul>
  </div>

  <div class="package premium">
    <div class="package-label">Premium <b class="price"><span>$</span>12.00</b></div>
    <ul class="package-rows">
      <li></li>
      <li><svg><use href="#tick"/></svg></li>
      <li></li>
      <li></li>
      <li><svg><use href="#tick"/></svg></li>
      <li></li>
      <li><svg><use href="#tick"/></svg></li>
      <li><svg><use href="#tick"/></svg></li>
      <li><svg><use href="#tick"/></svg></li>
      <li><svg><use href="#tick"/></svg></li>
    </ul>
  </div>

  <div class="car-photo" role="img" aria-label="Photo of a blue sports car with foam splash"></div>

  <div class="call-box">Call Us 0198-765-432</div>
  <div class="website">www.TidalCrestCarWash.com</div>
</section>
</body>
</html>
```